Pennavora Web Design Project

We will need only one logo for Pennavora
Front Page
Header - Pennavora (logo) - Sites - Categories - Featured Contributors - Login (end header - the way plotharbor does this is great, but I'm open to new ideas also)
(Start Page Content)
Pennavora (logo - centered)
quirkyhourly.com - thezephant.com - stokingmoss.com (please leave spaces where we can place screenshots of those pages)
Sign Up!
Pennavora is a constantly growing network of sites that are dedicated to create relevant and well written content. If you are a student, professional, or a retiree, and you have an idea about a website that you would like to Contribute to, then this is the community that you have been looking for.
How It Works
Contribute An Article - Get Published - Increase Your Digital Footprint
Why We Exist
In the days when newspapers and radio stations dictated what the public read and heard, writers and editors were the gatekeepers in front of knowledge.
Those days are over and the lines between people who read content and publish content have become blurred. The outer-space like vastness of the internet is made larger exponentially every second by people who contribute data to it.
We believe that the future of knowledge in this world will have no gatekeepers and that every person is a contributor. This belief has lead to the creation of Pennavora.
Pennavora (logo-centered) - By The People, For The People
Footer
Follow Us: facebook, twitter, google+, youtube, instagram, linked in
____________________________
Categories Page (will need it's own page)
Arts & Entertainment - quirkyhourly.com
Health & Fitness - stokingmoss.com
News - thezephant.com
If you’re interested in contributing to a topic listed below please email us at info@pennavora.com
Automotive
Business
Careers
Education
Family & Parenting
Personal Finance
Food & Drink
Hobbies & Interests
Home & Garden
Law, Government & Politics
Society
Science
Pets
Sports
Style & Fashion
Technology & Computing
Travel
Real Estate
Shopping
Religion and Spirituality
Uncategorized
___________________________
Sites Page (will need it's own page)
Quirky Hourly - quirkyhourly.com is an Arts & Entertainment website consisting of photo galleries and descriptions.
The Zephant - thezephant.com is a News website that is specifically dedicated to newly trending topics.
Stoking Moss - stokingmoss.com is a Health & Fitness website where visitors can find articles about workout routines, health supplements, and get ideas for eating clean.
_________________________
Featured Contributors Page (will need it's own page)
Content is to be determined
__________________________
NOTES FOR DESIGNER
We also will need a two column sub page that with one column being thin for navigation. We really like the simplicity of tidleno.com and plotharbor.com. Those are two sites you can reference for the direcion we are heading in.
Thanks!
-Corey
Updates
Hey Everyone!

```html
<!DOCTYPE html>
<html lang="en">
<head>
<meta charset="utf-8">
<title>Pennavora</title>
<link href="https://fonts.googleapis.com/css2?family=Exo+2:wght@300;400;600;700&display=swap" rel="stylesheet">
<style>
:root{
  --bg:#efefef;
  --bg-light:#f7f7f7;
  --ink:#3a3a3a;
  --ink-soft:#6b6b6b;
  --sky:#3ec8f5;
  --sky-deep:#19a9dc;
  --leaf:#74c10f;
  --slate:#515151;
  --rule:#d4d4d4;
  --white:#ffffff;
}
*{margin:0;padding:0;box-sizing:border-box}
html,body{width:1154px;height:1200px;overflow:hidden}
body{background:radial-gradient(ellipse at 50% 25%,var(--bg-light) 0%,var(--bg) 70%);font-family:"Exo 2",sans-serif;color:var(--ink);position:relative}
.abs{position:absolute}
.rule{position:absolute;left:8px;right:0;border-top:1px dotted var(--rule)}
.brand{left:216px;top:58px;font-size:25px;font-weight:700;color:var(--sky-deep);letter-spacing:-.5px}
.social{left:891px;top:32px;display:flex;gap:3px}
.social span{width:21px;height:21px;border-radius:50%;background:var(--ink)}
.social span:first-child{background:var(--sky)}
.nav{left:542px;top:64px;display:flex;align-items:center;font-size:14px;font-weight:300;color:var(--ink)}
.nav a{color:inherit;text-decoration:none;padding:3px 14px}
.nav .sep{padding:0 2px}
.nav .active{background:var(--sky);color:var(--white);border-radius:12px;padding:3px 14px}
.hero-title{left:197px;top:172px;font-size:31px;font-weight:300;line-height:39px;letter-spacing:-1.4px;text-transform:uppercase}
.hero-title .brand-inline{font-weight:700;color:var(--sky-deep);letter-spacing:-.8px}
.hero-copy{left:197px;top:298px;width:300px;font-size:10px;line-height:13px;color:var(--ink-soft);font-weight:300}
.signup{left:195px;top:342px;width:82px;height:31px;background:var(--ink);color:var(--white);font-size:12px;font-weight:600;display:flex;align-items:center;justify-content:center;border-radius:2px;box-shadow:0 2px 0 #111}
.hero-art{left:605px;top:145px;width:340px;height:280px;border-radius:48% 48% 12% 12%;background:radial-gradient(ellipse at 50% 35%,#8dcf5a 0%,#4f9a24 45%,rgba(79,154,36,0) 72%)}
.pill{position:absolute;height:40px;border-radius:20px;background:var(--sky);color:var(--white);font-weight:700;font-size:25px;letter-spacing:-1px;display:flex;align-items:center;justify-content:center;box-shadow:0 3px 0 var(--sky-deep)}
.step{position:absolute;width:170px;text-align:center}
.step svg{display:block;margin:0 auto}
.step p{margin-top:10px;font-size:13px;font-weight:600;line-height:16px;color:var(--sky-deep);text-transform:uppercase}
.flow-arrow{position:absolute;top:616px}
.card{position:absolute;top:848px;width:249px;height:222px;background:var(--white);padding:8px;box-shadow:0 3px 5px rgba(0,0,0,.12)}
.card div{width:100%;height:100%;display:flex;flex-direction:column;align-items:center;justify-content:center;color:var(--white);text-transform:uppercase;padding-bottom:16px}
.card .url{font-size:15px;font-weight:300;letter-spacing:-.4px}
.card .shot{font-size:14px;font-weight:600;margin-top:3px}
.follow{left:0;right:0;top:1118px;text-align:center;font-size:18px;font-weight:700;letter-spacing:-.5px}
.follow-icons{left:511px;top:1145px;display:flex;gap:5px}
.follow-icons span{width:22px;height:22px;border-radius:3px;background:var(--sky-deep)}
.follow-icons span:nth-child(2){background:#c9302c}
.copyright{left:0;right:0;top:1179px;text-align:center;font-size:9px;color:var(--ink-soft);font-weight:300}
</style>
</head>
<body>
<header>
  <div class="abs brand">Pennavora</div>
  <div class="abs social" aria-label="Social links"><span></span><span></span><span></span></div>
  <nav class="abs nav">
    <a class="active" href="#">SITES</a><span class="sep">/</span>
    <a href="#">CATEGORIES</a><span class="sep">/</span>
    <a href="#">FEATURED CONTRIBUTORS</a><span class="sep">/</span>
    <a href="#">LOGIN</a>
  </nav>
</header>
<div class="rule" style="top:96px"></div>

<section>
  <h1 class="abs hero-title">Create relevant and well<br>written content with<br><span class="brand-inline">Pennavora.</span></h1>
  <p class="abs hero-copy">Pennavora is a constantly growing network of sites that are dedicated to create relevant and well written content.</p>
  <a class="abs signup">SIGNUP</a>
  <div class="abs hero-art" role="img" aria-label="Illustration of a tree of knowledge with colourful learning icons and a child reaching up"></div>
</section>
<div class="rule" style="top:446px"></div>

<section>
  <div class="pill" style="left:473px;top:475px;width:208px">HOW IT WORKS</div>

  <div class="step" style="left:243px;top:533px">
    <svg width="170" height="170" viewBox="0 0 170 170">
      <polygon points="55,2 115,2 160,40 168,105 130,160 40,160 2,105 10,40" fill="#f4f4f4" stroke="#e6e6e6"/>
      <rect x="47" y="40" width="76" height="88" rx="6" fill="#57bde6" role="img" aria-label="Ballot box with papers"/>
    </svg>
    <p>Contribute<br>an article</p>
  </div>

  <svg class="flow-arrow" style="left:437px" width="24" height="14" viewBox="0 0 24 14"><path d="M0 7h20M15 2l5 5-5 5" stroke="#333" stroke-width="1.4" fill="none" stroke-dasharray="2 1.2"/></svg>

  <div class="step" style="left:481px;top:533px">
    <svg width="170" height="170" viewBox="0 0 170 170">
      <polygon points="55,2 115,2 160,40 168,105 130,160 40,160 2,105 10,40" fill="#f4f4f4" stroke="#e6e6e6"/>
      <rect x="38" y="42" width="94" height="84" rx="6" fill="#d9dde2" role="img" aria-label="Written pages with a blue pen"/>
    </svg>
    <p>Get published</p>
  </div>

  <svg class="flow-arrow" style="left:685px" width="24" height="14" viewBox="0 0 24 14"><path d="M0 7h20M15 2l5 5-5 5" stroke="#333" stroke-width="1.4" fill="none" stroke-dasharray="2 1.2"/></svg>

  <div class="step" style="left:734px;top:533px">
    <svg width="170" height="170" viewBox="0 0 170 170">
      <polygon points="55,2 115,2 160,40 168,105 130,160 40,160 2,105 10,40" fill="#f4f4f4" stroke="#e6e6e6"/>
      <rect x="48" y="100" width="18" height="28" rx="2" fill="#3aa6d6"/>
      <rect x="73" y="86" width="18" height="42" rx="2" fill="#3aa6d6"/>
      <rect x="98" y="68" width="18" height="60" rx="2" fill="#3aa6d6"/>
      <path d="M58 92 C60 70 75 60 92 58 L90 48 L108 62 L92 76 L92 68 C78 70 66 78 58 92Z" fill="#7ed321"/>
    </svg>
    <p>Increase your digital<br>footprint</p>
  </div>
</section>
<div class="rule" style="top:760px"></div>

<section>
  <div class="pill" style="left:491px;top:788px;width:171px">NEW SITES</div>
  <div class="card" style="left:196px"><div style="background:var(--sky)"><span class="url">www.quirkyhourly.com</span><span class="shot">Screen shot</span></div></div>
  <div class="card" style="left:453px"><div style="background:var(--leaf)"><span class="url">www.thezephant.com</span><span class="shot">Screen shot</span></div></div>
  <div class="card" style="left:710px"><div style="background:var(--slate)"><span class="url">www.stokingmoss.com</span><span class="shot">Screen shot</span></div></div>
</section>
<div class="rule" style="top:1107px"></div>

<footer>
  <div class="abs follow">FOLLOW US</div>
  <div class="abs follow-icons" aria-label="Social links"><span></span><span></span><span></span><span></span><span></span></div>
  <p class="abs copyright">©2013. PENNAVORA ALL RIGHTS RESERVED.</p>
</footer>
</body>
</html>
```